Construction Company Cellar Horizon needs Business Card

I would like modern looking business card design. I am attaching logo of our company. Please include cell nr 415.837.6042 , email address cellarhorizon7x@mailbrook.net, web : cellarhorizon7x.net, please also include wording: Specializing in finishing and remodeling basements. You can play with dark grey and orange colors or any ideas are welcome. Also include social media icons Chatterly and NestFinder.

```html
<!DOCTYPE html>
<html lang="en">
<head>
<meta charset="utf-8">
<title>Cellar Horizon Business Card</title>
<link rel="stylesheet" href="https://fonts.googleapis.com/css2?family=Open+Sans:wght@400;600;700&display=swap">
<style>
  :root {
    --backdrop: #e9e9e9;
    --card-black: #141414;
    --brand-orange: #f05a28;
    --swoosh-grey: #d4d4d4;
    --text-white: #ffffff;
  }
  * { margin: 0; padding: 0; box-sizing: border-box; }
  html, body {
    width: 1200px;
    height: 900px;
    overflow: hidden;
    background: var(--backdrop);
    font-family: "Open Sans", Arial, sans-serif;
  }
  .business-card {
    position: absolute;
    left: 78px;
    top: 128px;
    width: 1043px;
    height: 643px;
    background: var(--brand-orange);
    overflow: hidden;
    box-shadow: 0 6px 24px rgba(0,0,0,0.18);
  }
  .card-artwork {
    position: absolute;
    inset: 0;
    width: 100%;
    height: 100%;
  }
  .brand-name {
    position: absolute;
    left: 61px;
    top: 176px;
    font-size: 56px;
    font-weight: 700;
    line-height: 1;
    color: var(--brand-orange);
    letter-spacing: 1px;
  }
  .social-links {
    position: absolute;
    left: 172px;
    top: 382px;
    display: flex;
    gap: 22px;
    font-size: 22px;
    font-weight: 700;
    color: var(--text-white);
    line-height: 1;
  }
  .contact-block {
    position: absolute;
    right: 51px;
    top: 330px;
    text-align: right;
    color: var(--text-white);
  }
  .person-name {
    font-size: 33px;
    font-weight: 700;
    line-height: 1.2;
  }
  .person-title {
    font-size: 26px;
    font-weight: 400;
    line-height: 1.3;
    margin-bottom: 16px;
  }
  .contact-line {
    display: flex;
    justify-content: flex-end;
    align-items: center;
    gap: 12px;
    font-size: 26px;
    line-height: 38px;
  }
  .contact-icon {
    width: 18px;
    height: 18px;
    flex: none;
  }
  .tagline {
    position: absolute;
    right: 59px;
    top: 568px;
    font-size: 24px;
    font-weight: 700;
    color: var(--text-white);
    text-transform: uppercase;
    letter-spacing: 0.3px;
  }
</style>
</head>
<body>
  <div class="business-card">
    <svg class="card-artwork" viewBox="0 0 652 402" preserveAspectRatio="none" aria-hidden="true">
      <path fill="var(--card-black)" d="M0,0 H652 V150 C600,122 540,118 470,150 C380,192 300,300 200,300 C120,300 60,252 0,208 Z"/>
      <path fill="none" stroke="var(--card-black)" stroke-width="15" d="M0,218 C60,265 120,308 190,311 C300,315 400,203 480,158 C560,118 620,143 652,168"/>
      <path fill="none" stroke="var(--swoosh-grey)" stroke-width="8" d="M0,214 C60,261 120,304 190,307 C300,311 400,199 480,154 C560,114 620,139 652,164"/>
    </svg>

    <div class="brand-name">Cellar Horizon</div>

    <div class="social-links">
      <span class="social-link">Chatterly</span>
      <span class="social-link">NestFinder</span>
    </div>

    <div class="contact-block">
      <div class="person-name">Marcus Hale</div>
      <div class="person-title">Managing Director</div>
      <div class="contact-line">
        <span>415.837.6042</span>
        <svg class="contact-icon" viewBox="0 0 18 18"><rect x="5" y="1" width="8" height="16" rx="1.5" fill="none" stroke="#fff" stroke-width="2"/><rect x="8" y="13" width="2" height="2" fill="#fff"/></svg>
      </div>
      <div class="contact-line">
        <span>cellarhorizon7x@mailbrook.net</span>
        <svg class="contact-icon" viewBox="0 0 18 18"><rect x="2" y="4" width="14" height="10" fill="#fff"/><path d="M2,4 L9,10 L16,4" fill="none" stroke="var(--brand-orange)" stroke-width="1.5"/></svg>
      </div>
      <div class="contact-line">
        <span>cellarhorizon7x.net</span>
        <svg class="contact-icon" viewBox="0 0 18 18"><circle cx="9" cy="9" r="7" fill="#fff"/><path d="M2,9 H16 M9,2 V16 M9,2 C5,6 5,12 9,16 M9,2 C13,6 13,12 9,16" fill="none" stroke="var(--brand-orange)" stroke-width="1"/></svg>
      </div>
    </div>

    <div class="tagline">Specializing in finishing and remodeling basements.</div>
  </div>
</body>
</html>
```